Construction company yard sign

I would like a design for yard signs for my construction company. It will be used to put outside clients homes as we are working for them and will be used as advertisement for neighbors that are passing by the home.

The sign will be 18x24 and a plastic type material.

Target Market(s)

Homeowners

Font styles to use
Sans Serif

Requirements
Must have
• The most important thing about the sign is the visibility of the lettering and phone number 480-913-2647. The next would be Free roof Inspections. and then I would like to have these 3 words on there as well: Flat - Shingle - Tile

```html
<!DOCTYPE html>
<html lang="en">
<head>
<meta charset="utf-8">
<title>Halvorsen Construction Group – Yard Sign</title>
<link href="https://fonts.googleapis.com/css2?family=Bebas+Neue&family=Oswald:wght@500;600;700&display=swap" rel="stylesheet">
<style>
  :root {
    --brand-blue: #2ba3dc;
    --band-blue: #16aee6;
    --brand-red: #c0202e;
    --white: #ffffff;
    --sky-top: #3f86d8;
    --sky-bottom: #8cb8e6;
    --roof-dark: #3a3d42;
  }
  * { margin: 0; padding: 0; box-sizing: border-box; }
  html, body {
    width: 1200px;
    height: 900px;
    overflow: hidden;
    background: var(--white);
  }
  .sign {
    position: relative;
    width: 1200px;
    height: 900px;
    overflow: hidden;
    background: var(--white);
    font-family: "Bebas Neue", "Oswald", sans-serif;
  }
  .header {
    position: absolute;
    inset: 0 0 auto 0;
    height: 186px;
    background: var(--white);
  }
  .brand {
    position: absolute;
    left: 62px;
    top: 44px;
    display: flex;
    align-items: center;
    gap: 38px;
  }
  .brand-mark {
    width: 60px;
    height: 60px;
    background: var(--brand-blue);
    flex: none;
  }
  .brand-name {
    font-family: "Oswald", sans-serif;
    font-weight: 600;
    color: var(--brand-blue);
    text-transform: uppercase;
    line-height: 1;
  }
  .brand-name .line-main {
    display: block;
    font-size: 68px;
    letter-spacing: 8px;
  }
  .brand-name .line-sub {
    display: block;
    font-size: 22px;
    letter-spacing: 10px;
    margin-top: 8px;
  }
  .services-band {
    position: absolute;
    top: 0;
    right: 0;
    width: 626px;
    height: 186px;
  }
  .services-band svg { position: absolute; inset: 0; }
  .services {
    position: absolute;
    inset: 0 0 0 40px;
    display: flex;
    align-items: center;
    justify-content: center;
    font-family: "Oswald", sans-serif;
    font-weight: 700;
    font-size: 64px;
    color: var(--white);
    letter-spacing: 0.5px;
  }
  .services .dot {
    display: inline-block;
    width: 16px;
    height: 16px;
    border-radius: 50%;
    background: var(--white);
    margin: 0 14px;
  }
  .photo {
    position: absolute;
    top: 186px;
    left: 0;
    width: 1200px;
    height: 714px;
    background: linear-gradient(180deg, var(--sky-top) 0%, var(--sky-bottom) 32%, #6c7480 48%, var(--roof-dark) 62%, #2f3236 100%);
  }
  .offer {
    color: var(--white);
    text-transform: uppercase;
    font-weight: 400;
  }
  .offer-free {
    position: absolute;
    left: 50px;
    top: 294px;
    font-size: 380px;
    line-height: 0.8;
    letter-spacing: 8px;
    white-space: nowrap;
  }
  .offer-label {
    position: absolute;
    left: 52px;
    top: 588px;
    font-size: 96px;
    line-height: 1;
    letter-spacing: 4px;
    white-space: nowrap;
  }
  .phone-band {
    position: absolute;
    left: 0;
    top: 680px;
    width: 912px;
    height: 146px;
    background: var(--band-blue);
    display: flex;
    align-items: center;
    padding-left: 36px;
  }
  .phone-icon { width: 114px; height: 114px; flex: none; }
  .phone-number {
    font-family: "Oswald", sans-serif;
    font-weight: 700;
    font-size: 92px;
    color: var(--white);
    margin-left: 26px;
    letter-spacing: 5px;
    line-height: 1;
    white-space: nowrap;
  }
</style>
</head>
<body>
  <main class="sign">
    <div class="photo" role="img" aria-label="Photo of a dark tiled roof with a dormer window against a clear blue sky"></div>

    <header class="header">
      <div class="brand">
        <span class="brand-mark"></span>
        <span class="brand-name">
          <span class="line-main">Halvorsen</span>
          <span class="line-sub">Construction Group</span>
        </span>
      </div>
      <div class="services-band">
        <svg width="626" height="186" viewBox="0 0 626 186" aria-hidden="true">
          <polygon points="26,0 626,0 626,186 0,186" fill="var(--brand-red)"/>
        </svg>
        <p class="services">Flat<span class="dot"></span>Shingle<span class="dot"></span>Tile</p>
      </div>
    </header>

    <h1 class="offer">
      <span class="offer-free">Free</span>
      <span class="offer-label">Roof Inspections</span>
    </h1>

    <div class="phone-band">
      <svg class="phone-icon" viewBox="0 0 120 120" aria-hidden="true">
        <circle cx="60" cy="60" r="54" fill="none" stroke="var(--white)" stroke-width="7"/>
        <path d="M44 32c3-2 7-2 9 1l6 10c2 3 1 6-1 8l-4 3c3 7 8 12 15 16l3-4c2-2 5-3 8-1l10 6c3 2 3 6 1 9l-4 5c-3 3-8 4-13 2-17-6-30-19-36-36-2-5-1-10 2-13z" fill="var(--white)"/>
      </svg>
      <span class="phone-number">480-913-2647</span>
    </div>
  </main>
</body>
</html>
```